A small electrical company designed a vehicle wrap for the Corvan Haulmark 360

We designed a vehicle wrap for a small Los Angeles electrical company specializing in electrical repairs, air conditioning repair and installation, electric vehicle charging station installation, and electrical upgrades. Our clientele primarily serves residential and commercial customers. To stay within our budget, we chose a clear, eye-catching electrical and air conditioning logo that combined fonts and graphics to create a memorable impression.
Target Market(s)
electrical repair & installation, cooling&heating ,EV charger installation
Industry/Entity Type
electrical and Air conditioning
Requirements
Must have
- phone number:(555)4820173 Lic#:2048736 website www.quorvelectric.example
Nice to have
- my vehicle is Corvan haulmark 360 high roof 148'WB cargo van

```html
<!DOCTYPE html>
<html lang="en">
<head>
<meta charset="utf-8">
<title>Quorv Electric Solution Inc – Corvan Haulmark 360 Wrap</title>
<link href="https://fonts.googleapis.com/css2?family=Barlow+Semi+Condensed:wght@700&family=Montserrat:wght@600;700&family=Tinos:ital@1&display=swap" rel="stylesheet">
<style>
  :root {
    --backdrop: #dcdcdc;
    --navy: #2b3343;
    --navy-deep: #1f2533;
    --white: #ffffff;
    --orange: #f0962e;
    --window: #3a3f48;
    --tyre: #262b36;
    --hub: #a9adb4;
  }
  html, body { margin: 0; padding: 0; overflow: hidden; }
  body { width: 1089px; height: 1200px; background: var(--backdrop); position: relative; }
  .van-side { position: absolute; left: 0; width: 1089px; height: 560px; }
  .van-side--left { top: 0; }
  .van-side--right { top: 526px; }
  .wrap-white { fill: var(--white); }
  .wrap-navy { fill: var(--navy); }
  .wrap-rocker { fill: var(--navy-deep); }
  .cab-window { fill: var(--window); }
  .wheel-arch { fill: var(--navy-deep); }
  .tyre { fill: var(--tyre); }
  .hub { fill: var(--hub); }
  .hub-cap { fill: var(--tyre); }
  .mark-area { fill: var(--navy); }
  .mark-square { fill: var(--orange); }
  .mark-name { font-family: "Barlow Semi Condensed", sans-serif; font-weight: 700; font-size: 40px; fill: var(--white); text-anchor: middle; }
  .services { font-family: "Montserrat", sans-serif; font-weight: 700; font-size: 13.5px; fill: var(--white); letter-spacing: 0.5px; text-anchor: middle; }
  .company-name { font-family: "Barlow Semi Condensed", sans-serif; font-weight: 700; font-size: 44px; fill: var(--white); text-anchor: middle; }
  .tagline { font-family: "Tinos", serif; font-style: italic; font-size: 19px; fill: var(--orange); text-anchor: middle; }
  .tagline-rule { stroke: var(--orange); stroke-width: 1.5; }
  .phone { font-family: "Montserrat", sans-serif; font-weight: 700; font-size: 32px; fill: var(--white); text-anchor: middle; letter-spacing: 0.5px; }
  .website { font-family: "Montserrat", sans-serif; font-weight: 600; font-size: 20px; fill: var(--white); text-anchor: middle; }
  .website .accent { fill: var(--orange); }
  .licence { font-family: "Montserrat", sans-serif; font-weight: 600; font-size: 12px; fill: var(--navy); }
</style>
</head>
<body>

<svg width="0" height="0" style="position:absolute">
  <defs>
    <g id="van-body">
      <path class="wrap-white" d="M35,476 L35,400 L45,362 Q70,345 125,326 L180,300 Q240,220 320,165 Q400,128 480,125 L1000,120 Q1015,121 1020,140 L1040,430 L1042,476 Z"/>
      <path class="wrap-navy" d="M600,124 L1000,120 Q1015,121 1020,140 L1040,430 L1040,410 L600,410 Z"/>
      <path class="cab-window" d="M210,336 L262,246 Q285,222 348,218 L348,320 Q300,334 210,336 Z"/>
      <path class="wrap-rocker" d="M35,410 L1042,400 L1042,476 L35,476 Z"/>
      <circle class="wheel-arch" cx="176" cy="470" r="64"/>
      <circle class="wheel-arch" cx="755" cy="470" r="64"/>
      <circle class="tyre" cx="176" cy="470" r="54"/>
      <circle class="hub" cx="176" cy="470" r="34"/>
      <circle class="hub-cap" cx="176" cy="470" r="10"/>
      <circle class="tyre" cx="755" cy="470" r="54"/>
      <circle class="hub" cx="755" cy="470" r="34"/>
      <circle class="hub-cap" cx="755" cy="470" r="10"/>
    </g>
  </defs>
</svg>

<!-- Driver side (faces left) -->
<svg class="van-side van-side--left" viewBox="0 0 1089 560" xmlns="http://www.w3.org/2000/svg">
  <use href="#van-body"/>
  <g role="img" aria-label="Brand mark area">
    <rect class="mark-area" x="360" y="150" width="232" height="250"/>
    <rect class="mark-square" x="446" y="200" width="60" height="60"/>
    <text class="mark-name" x="476" y="320">QUORV</text>
  </g>
  <text class="services" x="800" y="154">ELECTRICAL REPAIR &amp; INSTALLATION</text>
  <text class="services" x="800" y="172">COOLING &amp; HEATING</text>
  <text class="services" x="800" y="190">EV CHARGER INSTALLATION</text>
  <text class="company-name" x="800" y="238">QUORV ELECTRIC</text>
  <text class="company-name" x="800" y="274">SOLUTION INC</text>
  <line class="tagline-rule" x1="670" y1="289" x2="706" y2="289"/>
  <text class="tagline" x="800" y="292">we power your homes</text>
  <line class="tagline-rule" x1="894" y1="289" x2="930" y2="289"/>
  <text class="phone" x="800" y="350">(555)4820173</text>
  <text class="website" x="800" y="375">www.<tspan class="accent">quorvelectric</tspan>.example</text>
  <text class="licence" x="218" y="384">LIC#: 2048736</text>
</svg>

<!-- Passenger side (faces right) -->
<svg class="van-side van-side--right" viewBox="0 0 1089 560" xmlns="http://www.w3.org/2000/svg">
  <use href="#van-body" transform="translate(1092,0) scale(-1,1)"/>
  <g role="img" aria-label="Brand mark area">
    <rect class="mark-area" x="500" y="150" width="232" height="250"/>
    <rect class="mark-square" x="586" y="200" width="60" height="60"/>
    <text class="mark-name" x="616" y="320">QUORV</text>
  </g>
  <text class="services" x="278" y="154">ELECTRICAL REPAIR &amp; INSTALLATION</text>
  <text class="services" x="278" y="172">COOLING &amp; HEATING</text>
  <text class="services" x="278" y="190">EV CHARGER INSTALLATION</text>
  <text class="company-name" x="278" y="238">QUORV ELECTRIC</text>
  <text class="company-name" x="278" y="274">SOLUTION INC</text>
  <line class="tagline-rule" x1="148" y1="289" x2="184" y2="289"/>
  <text class="tagline" x="278" y="292">we power your homes</text>
  <line class="tagline-rule" x1="372" y1="289" x2="408" y2="289"/>
  <text class="phone" x="278" y="350">(555)4820173</text>
  <text class="website" x="278" y="375">www.<tspan class="accent">quorvelectric</tspan>.example</text>
  <text class="licence" x="773" y="386">LIC#: 2048736</text>
</svg>

</body>
</html>
```